I need a website built for my modeling agency company.

On our website, a user can create a profile and we will submit it to thousands of modeling agents throughout the country.

In many cases, they will receive multiple offers from modeling agencies which allows them to pick and choose the contract that is best for them to launch their modeling career.

Some tag lines to consider using:

"Submit your profile to hundreds of modeling agents instantly!"

"Get found and become a star!"

We are: The Runway Guild.

Our Slogan: The World''s Largest Network of Fashion Models and Agents

What We Do: We are an agency with one of the largest networks of fashion professionals that are looking for new modeling talent. We host professional profiles for aspiring models, professional fashion models seeking work, modeling talent seekers, and top modeling agencies. We connect aspiring models with the top modeling agencies in the United States and abroad.

By submitting your FREE profile, you will be instantly introduced to the industry’s leading modeling agents. Within a few days, you could receive multiple, competing offers from modeling agencies that all want to launch your modeling career. Receiving multiple signing offers puts you in control of deciding which contract best suites you!

Reason: I've seen some good designs, but none that are 100% perfect. These are the ones that I like best so far (to give you some ideas): http://files.pixelvane.example/img/510372/820114/820114_4917263_510372_image.jpg http://files.pixelvane.example/img/510372/829305/829305_4926851_510372_image.jpg http://files.pixelvane.example/img/510372/51847/51847_4924097_510372_image.jpg http://files.pixelvane.example/img/510372/51847/51847_4919856_510372_image.jpg http://files.pixelvane.example/img/510372/823670/823670_4920438_510372_image.jpg

Target Market(s)

Aspiring models (mostly female, but some male)

Industry/Entity Type

Modeling Agency

Colors

Designer to choose colors to be used in the design.

Requirements
Nice to have
• Somewhere in the top half of the page, I would like there to be a small form for the visitor to fill out. This form will look as follows:

Title: Instantly contact hundreds of modeling agents who are looking for new talent and could make you a star!
Fields: First Name*, Last Name*, Age, Zip Code, Email Address*, Daytime Phone, Evening Phone, Comments.

Then, there will be a "submit" button to proceed to next step of form. Just below the "submit" button, should be the following verbiage: "You will have the opportunity to upload photo(s) and provide other pertinent information in next step."

```html
<!DOCTYPE html>
<html lang="en">
<head>
<meta charset="utf-8">
<title>The Runway Guild</title>
<link rel="stylesheet" href="https://fonts.googleapis.com/css2?family=Mulish:wght@400;600;700&family=Roboto+Condensed:wght@400;500&display=swap">
<style>
:root{
  --pink:#d81b83;
  --pink-dark:#b8146d;
  --ink:#1e1e1e;
  --text:#333;
  --muted:#888;
  --line:#dcdcdc;
  --panel:#fafafa;
  --page:#efefef;
  --field:#fff;
}
*{box-sizing:border-box;margin:0;padding:0}
html,body{width:1200px;height:1131px;overflow:hidden}
body{background:var(--page);font-family:"Mulish",sans-serif;color:var(--text);position:relative}
.abs{position:absolute}

.topbar{left:0;top:0;width:1200px;height:34px;background:#f8f8f8;border-bottom:1px solid #ddd}
.topbar .box{top:4px;height:24px;border:1px solid #d4d4d4;border-radius:3px;background:#fff;font-size:12px;color:#888;line-height:22px;padding:0 8px}
.account{left:750px;width:99px}
.search{left:855px;width:182px}
.topbar svg{position:absolute;right:6px;top:4px}

.brand{left:163px;top:52px}
.brand .name{display:flex;align-items:center;gap:10px;font-size:29px;font-weight:700;color:var(--ink);letter-spacing:.5px;line-height:1}
.brand .mark{width:22px;height:22px;background:var(--pink)}
.brand .slogan{font-size:9.5px;color:var(--ink);margin-top:14px}

.promo{right:163px;top:57px;font-size:17.5px;line-height:23px;color:var(--ink);white-space:nowrap}
.promo .cta{display:inline-block;position:relative;vertical-align:1px;margin-left:4px;background:var(--pink);color:#fff;font-size:12px;line-height:21px;height:21px;padding:0 24px 0 9px;border-radius:2px}
.promo .cta svg{position:absolute;right:7px;top:6px}

.nav{left:163px;top:124px;width:874px;height:37px;background:#fff;border:1px solid #e2e2e2;box-shadow:0 2px 3px rgba(0,0,0,.08);display:flex;font-family:"Roboto Condensed",sans-serif;font-size:14px;color:var(--ink)}
.nav a{display:block;padding:0 9.5px;line-height:36px;color:inherit;text-decoration:none}
.nav a.active{background:var(--pink);color:#fff;padding:0 14px}

.hero{left:163px;top:173px;width:600px;height:382px;border-radius:3px;background:linear-gradient(135deg,#d9d9dc 0%,#8b8c97 45%,#3b3f63 75%,#25295a 100%)}
.hero .arrow{position:absolute;width:31px;height:31px;border-radius:50%;background:#fff;box-shadow:0 1px 3px rgba(0,0,0,.3)}
.hero .arrow svg{position:absolute;left:10px;top:10px}

.signup{left:773px;top:172px;width:264px;height:384px;background:var(--panel);border:1px solid var(--line);border-radius:3px;padding:11px 11px 0 15px}
.signup h2{font-size:12px;font-weight:600;line-height:17px;color:var(--ink);letter-spacing:-.25px}
.signup h2 em{font-style:normal;color:var(--pink)}
.field{position:absolute;left:16px;width:231px;height:26px;background:var(--field);border:1px solid #d2d2d2;border-radius:3px;font-size:10.5px;color:#333;line-height:24px;padding-left:9px}
.field.half{width:113px}
.field.right{left:134px}
.field .req{color:var(--pink)}
.field.comments{height:51px;line-height:1;padding-top:8px}
.submit{position:absolute;right:9px;top:12px;background:var(--pink);color:#fff;font-weight:700;font-size:12px;width:66px;height:27px;line-height:27px;text-align:center;border-radius:2px}
.signup .note{position:absolute;left:19px;top:343px;font-family:Arial,sans-serif;font-size:10px;line-height:16px;color:#111;letter-spacing:-.2px}
.signup .note span{color:var(--pink)}

.panel{background:var(--panel);border:1px solid var(--line);border-radius:3px}
.showcase{left:163px;top:567px;width:662px;height:440px}
.section-title{position:absolute;left:16px;font-size:18px;color:var(--ink);font-weight:400}
.pager{position:absolute;right:18px;display:flex;gap:3px}
.pager i{width:14px;height:14px;border-radius:50%;background:#111;display:block;position:relative}
.pager i svg{position:absolute;left:3px;top:3px}
.tiles{position:absolute;left:16px;display:flex;gap:9px}
.agency{width:150px;height:139px}
.agency .logo{height:93px;background:radial-gradient(circle at 50% 40%,#555,#1a1a1a);color:#eee;font-size:18px;text-align:center;line-height:93px}
.agency .info{height:46px;background:var(--pink);color:#fff;padding:7px 8px}
.agency .info b{font-weight:600;font-size:12px;display:block}
.agency .info small{font-size:9px;display:block;margin-top:4px}
.model{width:150px;height:182px;position:relative}
.model .cap{position:absolute;left:0;bottom:0;width:100%;height:19px;background:rgba(40,40,40,.7);color:#fff;font-size:11.5px;line-height:19px;padding-left:8px}

.sidebar{left:840px;top:567px;width:197px;height:440px}
.sidebar h3{font-size:16px;font-weight:400;color:var(--ink);padding:15px 15px 8px}
.profile{border-bottom:1px solid var(--line);padding:4px 15px 6px;height:59px;font-family:Arial,sans-serif}
.profile a{color:var(--pink);font-family:"Mulish",sans-serif;font-size:13px;text-decoration:none;display:block;margin-bottom:4px}
.profile p{font-size:8.8px;color:#111;line-height:14.5px;letter-spacing:-.1px}
.profile.short{height:54px}
.profile.last{border-bottom:none}
.newsletter{position:absolute;left:0;top:335px;width:100%;border-top:1px solid var(--line)}
.newsletter h3{padding-top:10px}
.newsletter .email{margin:0 14px;height:24px;border:1px solid #ccc;border-radius:3px;background:#fff;font-size:8.5px;line-height:22px;padding-left:10px;color:#555}
.newsletter .btn{margin:11px 0 0 15px;display:inline-block;background:var(--pink);color:#fff;font-size:13px;padding:0 13px;line-height:23px;border-radius:2px}

.footer{left:163px;top:1024px;width:874px;border-top:1px solid #ddd;text-align:center}
.footer nav{margin-top:14px;font-family:"Roboto Condensed",sans-serif;font-size:11px;color:#111}
.footer nav span{margin:0 5px}
.footer .copy{font-size:8.5px;color:#333;margin-top:8px}
.social{display:flex;justify-content:center;gap:5px;margin-top:14px}
.social i{width:27px;height:27px;border-radius:50%;background:#111;display:block}
</style>
</head>
<body>

<header class="abs topbar">
  <div class="abs box account">My Account
    <svg width="12" height="13" viewBox="0 0 12 13"><circle cx="6" cy="4" r="3" fill="#999"/><path d="M0 13c0-4 3-5.5 6-5.5s6 1.5 6 5.5z" fill="#999"/></svg>
  </div>
  <div class="abs box search">Search
    <svg width="14" height="14" viewBox="0 0 14 14"><circle cx="6" cy="6" r="4.5" fill="none" stroke="#aaa" stroke-width="1.6"/><path d="M9.5 9.5l3.5 3.5" stroke="#aaa" stroke-width="1.8"/></svg>
  </div>
</header>

<div class="abs brand">
  <div class="name"><span class="mark"></span>The Runway Guild</div>
  <div class="slogan">The World's Largest Network of Fashion Models and Agents</div>
</div>

<div class="abs promo">
  Submit your profile to hundreds of<br>modeling agents instantly!<span class="cta">Click Here<svg width="8" height="9" viewBox="0 0 8 9"><path d="M0 0l8 4.5L0 9z" fill="#fff"/></svg></span>
</div>

<nav class="abs nav">
  <a class="active" href="#">HOME</a>
  <a href="#">ABOUT US</a>
  <a href="#">MODELING AGENCIES</a>
  <a href="#">BECOME A MODEL</a>
  <a href="#">MEN</a>
  <a href="#">WOMAN</a>
  <a href="#">BLOG</a>
  <a href="#">CONTACT US</a>
</nav>

<section class="abs hero" role="img" aria-label="Runway photo of models in sunglasses and blue dresses backstage">
  <span class="arrow" style="left:17px;top:172px"><svg width="10" height="11" viewBox="0 0 10 11"><path d="M8 0v11L0 5.5z" fill="#111"/></svg></span>
  <span class="arrow" style="left:553px;top:172px"><svg width="10" height="11" viewBox="0 0 10 11"><path d="M2 0v11l8-5.5z" fill="#111"/></svg></span>
</section>

<aside class="abs signup">
  <h2>Instantly contact hundreds of modeling agents who are looking for new talent and could make you a <em>star!</em></h2>
  <div class="field" style="top:72px">First Name*</div>
  <div class="field" style="top:106px">Last Name*</div>
  <div class="field" style="top:140px">Age</div>
  <div class="field" style="top:175px">Zip Code</div>
  <div class="field" style="top:211px">Email Address<span class="req">*</span></div>
  <div class="field half" style="top:247px">Daytime Phone</div>
  <div class="field half right" style="top:247px">Evening Phone</div>
  <div class="field comments" style="top:283px">Comments<span class="submit">SUBMIT</span></div>
  <p class="note">You will have the opportunity to upload photo<b>(s)</b><br>and provide other pertinent information in <span>next step</span></p>
</aside>

<main class="abs panel showcase">
  <h2 class="section-title" style="top:13px">Modeling Agencies</h2>
  <div class="pager" style="top:23px">
    <i><svg width="8" height="8" viewBox="0 0 8 8"><path d="M6 0v8L0 4z" fill="#fff"/></svg></i>
    <i><svg width="8" height="8" viewBox="0 0 8 8"><path d="M2 0v8l6-4z" fill="#fff"/></svg></i>
  </div>
  <div class="tiles" style="top:45px">
    <div class="agency"><div class="logo">LOGO HERE</div><div class="info"><b>Lorem Ipsum</b><small>New York, USA</small></div></div>
    <div class="agency"><div class="logo">LOGO HERE</div><div class="info"><b>Lorem Ipsum</b><small>New York, USA</small></div></div>
    <div class="agency"><div class="logo">LOGO HERE</div><div class="info"><b>Lorem Ipsum</b><small>New York, USA</small></div></div>
    <div class="agency"><div class="logo">LOGO HERE</div><div class="info"><b>Lorem Ipsum</b><small>New York, USA</small></div></div>
  </div>

  <h2 class="section-title" style="top:201px">Models</h2>
  <div class="pager" style="top:210px">
    <i><svg width="8" height="8" viewBox="0 0 8 8"><path d="M6 0v8L0 4z" fill="#fff"/></svg></i>
    <i><svg width="8" height="8" viewBox="0 0 8 8"><path d="M2 0v8l6-4z" fill="#fff"/></svg></i>
  </div>
  <div class="tiles" style="top:233px">
    <div class="model" role="img" aria-label="Portrait of a model with a pink flower headdress" style="background:linear-gradient(160deg,#f1c8cc,#e8d2c4 55%,#d8b7a8)"><span class="cap">LOREM IPSUM</span></div>
    <div class="model" role="img" aria-label="Portrait of a model with long brown hair in red" style="background:linear-gradient(160deg,#d8cbb6,#8a5a44 50%,#b02a2a)"><span class="cap">LOREM IPSUM</span></div>
    <div class="model" role="img" aria-label="Portrait of a model with wavy auburn hair" style="background:linear-gradient(160deg,#6a3a3f,#c9706e 55%,#f0b4a8)"><span class="cap">LOREM IPSUM</span></div>
    <div class="model" role="img" aria-label="Portrait of a male model in a dark shirt" style="background:linear-gradient(160deg,#c9ccd0,#8a8d8f 50%,#3b4640)"><span class="cap">LOREM IPSUM</span></div>
  </div>
</main>

<aside class="abs panel sidebar">
  <h3>Newest Model Profiles</h3>
  <div class="profile"><a href="#">Liesbeth</a><p>Location: Spain | Sex: female<br>Jobs: Photo shoot Advertising production</p></div>
  <div class="profile"><a href="#">Patrick</a><p>Location: Spain | Sex: female<br>Jobs: Photo shoot Advertising production</p></div>
  <div class="profile"><a href="#">Carla</a><p>Location: Spain | Sex: female<br>Jobs: Photo shoot Advertising production</p></div>
  <div class="profile"><a href="#">Ricky</a><p>Location: Spain | Sex: female<br>Jobs: Photo shoot Advertising production</p></div>
  <div class="profile short last"><a href="#">Ozge</a><p>Location: Spain | Sex: female</p></div>
  <div class="newsletter">
    <h3>Newsletter Subscribe</h3>
    <div class="email">Email Address</div>
    <span class="btn">Subscribe</span>
  </div>
</aside>

<footer class="abs footer">
  <nav>HOME<span>|</span>ABOUT US<span>|</span>MODELING AGENCIES<span>|</span>BECOME A MODEL<span>|</span>MEN<span>|</span>WOMAN<span>|</span>BLOG<span>|</span>CONTACT US</nav>
  <p class="copy">Copyrights 2013 The Runway Guild, All Rights Reserved.</p>
  <div class="social">
    <i role="img" aria-label="Social network link"></i>
    <i role="img" aria-label="Social network link"></i>
    <i role="img" aria-label="Social network link"></i>
  </div>
</footer>

</body>
</html>
```